KELVO SMS Web Design Project

We need a new web design to replace the current one. See the current one: http://www.sms.quorvel.org/quorvel

The new name instead of Tandril Communications is changed to Kelvo SMS

Make provisions for were members can advertise their products / business.

```html
<!DOCTYPE html>
<html lang="en">
<head>
<meta charset="utf-8">
<title>Kelvo SMS</title>
<link rel="stylesheet" href="https://fonts.googleapis.com/css2?family=Source+Sans+3:wght@300;400;600;700&display=swap">
<style>
  :root {
    --blue: #2266b8;
    --blue-deep: #1b5aa8;
    --blue-light: #5da3e3;
    --nav-active: #2e7bd6;
    --text: #555;
    --rule: #d4d4d4;
    --band: #f3f5f8;
    --white: #fff;
    --black: #111;
  }
  * { margin: 0; padding: 0; box-sizing: border-box; }
  html, body { width: 1157px; height: 1200px; overflow: hidden; background: var(--white); }
  body { font-family: "Source Sans 3", sans-serif; }
  .page { position: relative; width: 1024px; height: 1062px; transform: scale(1.1299); transform-origin: 0 0; }
  .page > * { position: absolute; }

  .top-strip { left: 0; top: 0; width: 1024px; height: 6px; background: #e8e8e8; }
  .brand { left: 48px; top: 40px; }
  .brand-name { font-size: 37px; font-weight: 600; color: var(--blue); line-height: 1; letter-spacing: -0.5px; }
  .brand-slogan { margin-left: 67px; font-size: 14px; font-weight: 300; color: var(--blue); }
  .main-nav { left: 374px; top: 78px; display: flex; align-items: center; }
  .main-nav a { font-size: 13.5px; color: var(--blue); text-decoration: none; height: 27px; line-height: 27px; padding: 0 15px; margin-right: 11px; }
  .main-nav a.active { background: var(--nav-active); color: var(--white); border-radius: 3px; }

  .hero { left: 0; top: 125px; width: 1024px; height: 352px; border-top: 3px solid var(--blue-deep);
    background: radial-gradient(ellipse 70% 95% at 62% 30%, var(--blue-light) 0%, #3f88d4 40%, var(--blue-deep) 100%); }
  .hero-title { left: 51px; top: 190px; font-size: 28px; font-weight: 300; color: var(--white); }
  .hero-text { left: 53px; top: 233px; width: 355px; font-size: 11.5px; line-height: 18px; color: var(--white); }
  .btn { top: 342px; height: 32px; line-height: 32px; font-size: 13px; padding-left: 17px; border-radius: 3px; }
  .btn-send { left: 54px; width: 142px; background: var(--white); color: #444; }
  .btn-book { left: 204px; width: 138px; background: var(--black); color: var(--white); }
  .btn svg { position: absolute; right: 14px; top: 11px; }
  .hero-devices { left: 497px; top: 158px; width: 325px; height: 367px; border-radius: 26px;
    background: linear-gradient(160deg, #2a2a2a 0%, #0d0d0d 60%, #3b3b3b 100%); }
  .hero-envelopes { left: 820px; top: 200px; width: 190px; height: 215px; border-radius: 40px;
    background: radial-gradient(ellipse at center, rgba(140,195,245,0.35), rgba(140,195,245,0)); }

  .section-title { font-size: 24px; font-weight: 400; color: var(--blue); }
  .welcome-title { left: 40px; top: 515px; }
  .welcome-rule { left: 40px; top: 549px; width: 928px; height: 1px; background: var(--rule); }
  .welcome-text { left: 40px; top: 559px; width: 930px; font-size: 11.5px; line-height: 18px; color: var(--text); }
  .welcome-text p + p { margin-top: 18px; }
  .featured-title { left: 38px; top: 750px; }

  .featured-band { left: 0; top: 790px; width: 1024px; height: 218px; background: linear-gradient(#f1f3f6, #fafbfc); }
  .feature { top: 814px; width: 225px; }
  .feature h3 { font-size: 18px; font-weight: 400; color: var(--blue); margin-bottom: 5px; }
  .feature p { font-size: 11.5px; line-height: 18px; color: var(--blue); }
  .feature .read-more { display: inline-block; margin-top: 18px; font-size: 13.5px; font-weight: 600; color: var(--blue); text-decoration: none; }
  .feature-1 { left: 110px; } .feature-2 { left: 437px; } .feature-3 { left: 779px; }
  .feature-icon-photo { left: 41px; top: 818px; width: 54px; height: 84px; border-radius: 7px;
    background: linear-gradient(#2b2b2b, #2b2b2b 12%, #4d8fe0 13%, #2e72cc 80%, #1c1c1c 81%); }
  .feature-icon-handset { left: 366px; top: 812px; }
  .feature-icon-bubble { left: 686px; top: 812px; }

  .site-footer { left: 0; top: 1008px; width: 1024px; height: 54px; background: var(--blue-deep); }
  .site-footer p { position: absolute; left: 30px; top: 17px; font-size: 11.5px; color: var(--white); }
</style>
</head>
<body>
<div class="page">
  <div class="top-strip"></div>

  <div class="brand">
    <div class="brand-name">Kelvo SMS</div>
    <div class="brand-slogan">your slogan here..</div>
  </div>
  <nav class="main-nav">
    <a class="active" href="#">About Us</a>
    <a href="#">Product &amp; Services</a>
    <a href="#">Pricing</a>
    <a href="#">Client Login</a>
    <a href="#">Sign Up</a>
    <a href="#">Contact Us</a>
  </nav>

  <div class="hero"></div>
  <div class="hero-envelopes" role="img" aria-label="Flying envelopes decoration"></div>
  <h1 class="hero-title">Your Partner to Reach the World</h1>
  <p class="hero-text">Brightwave eSolutions is a web service company, offering a wide range of services which range from designing and development, that is covering almost all the fields in the best possible way.<br>We act in accordance with the Industry certified processes to deliver the best to our clients all over the world.</p>
  <a class="btn btn-send">SEND SMS NOW
    <svg width="7" height="11" viewBox="0 0 7 11"><path d="M1 1l4.5 4.5L1 10" fill="none" stroke="#888" stroke-width="1.6"/></svg></a>
  <a class="btn btn-book">BOOK YOU NO.
    <svg width="7" height="11" viewBox="0 0 7 11"><path d="M1 1l4.5 4.5L1 10" fill="none" stroke="#fff" stroke-width="1.6"/></svg></a>
  <div class="hero-devices" role="img" aria-label="Two smartphones showing a message envelope and a chat screen"></div>

  <h2 class="section-title welcome-title">Welcome to Kelvo SMS</h2>
  <div class="welcome-rule"></div>
  <div class="welcome-text">
    <p>Brightwave eSolutions is a web service company, offering a wide range of services which range from designing and development, that is covering almost all the fields in the best possible way. To be the best we know what and how to present beautifully the working of the client's need and their advantages be highlighted. We act in accordance with the Industry certified processes to deliver the best to our clients all over the world.</p>
    <p>Thus, Wanna get ahead in the competition with other websites…. Brightwave esolutions provide you with an attractive and most convincing website to enhance your marketing goals. The only way to success is through the right path and that's what we provide you. None of the other companies has the result we do. So stick to the best that's how you will be the best don't opt for the second best. Our expertise does not limit itself to web development but also it includes Web Hosting, Search Engine Optimization, E-Commerce. We partner hundreds of organization to enhance their business, marketing and profit goals.</p>
  </div>

  <h2 class="section-title featured-title">Featured &amp; Products</h2>
  <div class="featured-band"></div>

  <div class="feature-icon-photo" role="img" aria-label="Smartphone with blue screen"></div>
  <svg class="feature-icon-handset" width="58" height="88" viewBox="0 0 58 88" aria-hidden="true">
    <rect x="2" y="2" width="54" height="84" rx="8" fill="none" stroke="#2f62b0" stroke-width="4"/>
    <rect x="10" y="11" width="38" height="38" fill="#4a7fd0"/>
    <g fill="#4a7fd0">
      <rect x="16" y="56" width="5" height="5"/><rect x="27" y="56" width="5" height="5"/><rect x="38" y="56" width="5" height="5"/>
      <rect x="16" y="65" width="5" height="5"/><rect x="27" y="65" width="5" height="5"/><rect x="38" y="65" width="5" height="5"/>
      <rect x="16" y="74" width="5" height="5"/><rect x="27" y="74" width="5" height="5"/><rect x="38" y="74" width="5" height="5"/>
    </g>
  </svg>
  <svg class="feature-icon-bubble" width="80" height="80" viewBox="0 0 80 80" aria-hidden="true">
    <path d="M8 3h64a5 5 0 0 1 5 5v46a5 5 0 0 1-5 5H32L22 75 19 59H8a5 5 0 0 1-5-5V8a5 5 0 0 1 5-5z" fill="#fff" stroke="#2f62b0" stroke-width="4" stroke-linejoin="round"/>
    <g stroke="#111" stroke-width="5" stroke-linecap="round">
      <line x1="14" y1="16" x2="66" y2="16"/><line x1="14" y1="26" x2="66" y2="26"/>
      <line x1="14" y1="36" x2="66" y2="36"/><line x1="14" y1="46" x2="52" y2="46"/>
    </g>
  </svg>

  <article class="feature feature-1">
    <h3>Featured Services</h3>
    <p>Brightwave eSolutions provides you the Search Engine Optimization making your website search engine friendly. So that the website can achieve top position and ranking in the Internet searches and thereby increasing.</p>
    <a class="read-more" href="#">READ MORE &nbsp;›</a>
  </article>
  <article class="feature feature-2">
    <h3>Featured Services</h3>
    <p>Brightwave eSolutions provides you the Search Engine Optimization making your website search engine friendly. So that the website can achieve top position and ranking in the Internet searches and thereby increasing.</p>
    <a class="read-more" href="#">READ MORE &nbsp;›</a>
  </article>
  <article class="feature feature-3">
    <h3>Featured Services</h3>
    <p>Brightwave eSolutions provides you the Search Engine Optimization making your website search engine friendly. So that the website can achieve top position and ranking in the Internet searches and thereby increasing.</p>
    <a class="read-more" href="#">READ MORE &nbsp;›</a>
  </article>

  <footer class="site-footer"><p>© 2012 Company Name &nbsp;|&nbsp; All right reserved</p></footer>
</div>
</body>
</html>
```